会社や店舗の収支を毎日把握管理することで、販売、労務、キャッシュフローの管理が毎日出来るシステムです。
現在複数の地方銀行とのビジネスマッチングが進んでおり、今回のチラシは、銀行の渉外担当者が、顧客先にて置いてくるチラシです。その後、顧客より興味がある等レスがあった際はこちらから連絡して契約につなげます。
ですので、このシステムのことが理解出来ていない、銀行員や顧客でもまずはA4の表裏で興味を持ってもらえて問い合わせがもらえることが目的のものです。
今後銀行ごとにオリジナルのデザインの要望が来ることも考えられ、その際は継続的に仕事を依頼する予定です。
デザインの変わらない項目などの変更程度は納品後も対応頂ける方がありがたいです。もちろんデザインが変わる際は別途報酬をお支払いします。

```html
<!DOCTYPE html>
<html lang="ja">
<head>
<meta charset="utf-8">
<title>sumica — クラウド営業収支管理システム</title>
<link href="https://fonts.googleapis.com/css2?family=Noto+Sans+JP:wght@400;500;700;900&family=Nunito:wght@800;900&display=swap" rel="stylesheet">
<style>
  :root{
    --navy:#1f2d6b;
    --blue:#1b9be0;
    --bar:#d4d6da;
    --white:#ffffff;
    --ink:#333a4d;
  }
  *{margin:0;padding:0;box-sizing:border-box}
  html,body{width:849px;height:1200px;overflow:hidden;background:var(--white)}
  body{font-family:"Noto Sans JP",sans-serif;color:var(--ink);position:relative}

  .header{position:absolute;left:0;top:0;width:849px;height:290px;background:var(--navy)}
  .header__kicker{position:absolute;left:40px;top:40px;color:var(--white);font-weight:700;font-size:26px;letter-spacing:2px}
  .header__strip{position:absolute;left:0;top:140px;width:690px;height:130px;background:var(--white)}
  .header__product{position:absolute;left:34px;top:118px;font-family:"Nunito",sans-serif;font-weight:900;font-size:150px;line-height:1;color:var(--navy);letter-spacing:2px}
  .header__brand{position:absolute;left:706px;top:150px;width:116px;height:116px;background:var(--white);display:flex;align-items:center;justify-content:center;gap:6px;flex-direction:column}
  .brand__mark{width:22px;height:22px;background:var(--navy)}
  .brand__name{font-weight:900;font-size:15px;color:var(--navy);letter-spacing:1px}

  .visual{position:absolute;left:0;top:290px;width:849px;height:365px}
  .visual__lead{position:absolute;left:60px;top:18px;color:var(--navy);font-weight:900;font-size:34px;line-height:1.35;letter-spacing:1px}
  .visual__lead em{font-style:normal;color:var(--blue);font-size:42px}
  .visual__chart{position:absolute;left:40px;top:110px}

  .merits{position:absolute;left:0;top:655px;width:849px;height:545px;background:var(--navy)}
  .merits__title{position:absolute;left:0;top:40px;width:100%;text-align:center;color:var(--white);font-weight:700;font-size:28px;letter-spacing:3px}
  .merits__list{position:absolute;left:37px;top:100px;width:775px;display:flex;gap:25px}
  .merit{width:175px;height:390px;background:var(--white);position:relative;padding:0 14px}
  .merit__head{margin:18px -4px 0;background:var(--navy);color:var(--white);font-weight:700;font-size:15px;line-height:1.3;text-align:center;padding:9px 4px;border:2px solid var(--white);outline:1px solid var(--navy)}
  .merit__text{margin-top:38px;font-size:12.5px;line-height:1.75;color:var(--ink)}
  .merit__text + .merit__text{margin-top:12px}
  .merit__fig{position:absolute;left:50%;transform:translateX(-50%)}
  .merits__rule{position:absolute;left:37px;right:37px;bottom:32px;height:2px;background:var(--white)}
</style>
</head>
<body>
  <header class="header">
    <p class="header__kicker">クラウド営業収支管理システム</p>
    <div class="header__strip"></div>
    <h1 class="header__product">sumica</h1>
    <div class="header__brand">
      <span class="brand__mark"></span>
      <span class="brand__name">KAIKEI LAB</span>
    </div>
  </header>

  <section class="visual">
    <p class="visual__lead">経営に必要な情報を<em>見える化</em>。<br>毎日、一目で把握できます。</p>
    <svg class="visual__chart" width="770" height="220" viewBox="0 0 770 220">
      <g fill="var(--bar)">
        <rect x="20" y="90" width="34" height="100"/>
        <rect x="110" y="110" width="34" height="80"/>
        <rect x="200" y="70" width="34" height="120"/>
        <rect x="245" y="40" width="34" height="150"/>
        <rect x="290" y="95" width="34" height="95"/>
        <rect x="360" y="60" width="34" height="130"/>
        <rect x="405" y="30" width="34" height="160"/>
        <rect x="450" y="85" width="34" height="105"/>
        <rect x="520" y="100" width="34" height="90"/>
        <rect x="565" y="45" width="34" height="145"/>
        <rect x="610" y="75" width="34" height="115"/>
        <rect x="655" y="20" width="34" height="170"/>
      </g>
      <rect x="65" y="25" width="34" height="165" fill="var(--blue)"/>
      <g font-family="Noto Sans JP, sans-serif" font-size="13" font-weight="700" fill="var(--blue)" text-anchor="middle">
        <text x="82" y="212">販売管理</text>
        <text x="262" y="212">労務管理</text>
        <text x="422" y="212">在庫管理</text>
        <text x="605" y="212">キャッシュフロー管理</text>
      </g>
    </svg>
  </section>

  <section class="merits">
    <h2 class="merits__title">4つの導入メリット</h2>
    <div class="merits__list">
      <article class="merit">
        <h3 class="merit__head">毎日情報更新</h3>
        <p class="merit__text">毎日、自動で見やすいダッシュボードに反映します。</p>
        <p class="merit__text">より迅速な意思決定、スピーディな経営判断が可能になります。</p>
      </article>
      <article class="merit">
        <h3 class="merit__head">システム導入不要</h3>
        <p class="merit__text">既存のシステムにあるデータを加工・連携するツールなため、導入手続き、運用にかかる多額の追加投資は必要ありません。</p>
        <svg class="merit__fig" style="bottom:30px" width="90" height="90" viewBox="0 0 90 90">
          <circle cx="45" cy="45" r="32" fill="none" stroke="var(--bar)" stroke-width="20"/>
          <path d="M45 13 A32 32 0 0 1 77 45" fill="none" stroke="#eceef1" stroke-width="20"/>
        </svg>
      </article>
      <article class="merit">
        <h3 class="merit__head">データ集計・分析<br>・可視化を1つで</h3>
        <p class="merit__text" style="margin-top:28px">独立したデータを集め、ストレージへ入れておくだけで、今まで出来なかったクロス分析が可能になります。</p>
        <p class="merit__text">360度さまざまな視点でビジネスの分析ができ、今まで見えなかった課題が浮き彫りになります。</p>
      </article>
      <article class="merit">
        <h3 class="merit__head">業務効率UP</h3>
        <svg class="merit__fig" style="top:76px" width="60" height="60" viewBox="0 0 64 64">
          <circle cx="32" cy="32" r="27" fill="none" stroke="var(--bar)" stroke-width="3"/>
          <path d="M32 5 A27 27 0 1 1 6.3 23.7" fill="none" stroke="var(--navy)" stroke-width="3"/>
          <text x="32" y="37" text-anchor="middle" font-family="Noto Sans JP, sans-serif" font-size="13" fill="var(--ink)">80%</text>
        </svg>
        <p class="merit__text" style="margin-top:86px">やる事はデータを日々ストレージに入れるだけです。</p>
        <p class="merit__text">使い方も非常にシンプル、特別なスキルは必要ありません。</p>
        <p class="merit__text">業務効率化にとどまらず、人件費削減にも貢献します。</p>
      </article>
    </div>
    <div class="merits__rule"></div>
  </section>
</body>
</html>
```